5 Planner Covers for Teacher Planners

Hello,
I currently run a Speech-Language Pathologist website and have created a planner for my fellow Speech Therapist. I would like someone to create 5 different planner covers so my followers will have different options to choose from.
Here is my planner from last year to give you an idea of what the planner will look like http://www.talkwellnook.example/free-slp-planner/
My followers are mostly women aged 25-50. However, I don't want the covers to be overly girly or excessive with flowers. Simple is better.
I'd also like there to be an editable text box to allow the Speech Therapist to type their name on their cover if they wish.
Planner Cover can say any of the following: SLP Planner, Planner, Speech Therapy Planner, Speech-Language Pathologist (maybe this title could be editable as well??).
To give you an idea I have uploaded a screenshot of last year's planners cover that I made myself.
What I am looking for:
-Size 8.5" by 11"
-5 different planner covers
-1 gender-neutral cover
-simple design
-limited flowers (or overly girly
-text box to add a personal name
-Possible titles: SLP Planner, Planner, Speech Therapy Planner, Speech-Language Pathologist (maybe this title could be editable as well??)
Target Market(s)
Women aged 25-50
Colors
Designer to choose colors to be used in the design.
Requirements
Must have
- What I am looking for:
-Size 8.5" by 11"
-1 gender-neutral cover
-simple design
Nice to have
- I've uploaded some that I like from Craftly to give you an idea.
Here is my craftly store https://www.craftly.example/shop/QuietMeadowHome to give you an idea of things I like.
I like Marla Hensley and her simple elegant rustic style.

```html
<!DOCTYPE html>
<html lang="en">
<head>
<meta charset="utf-8">
<title>Speech Therapy Planner Covers</title>
<link rel="stylesheet" href="https://fonts.googleapis.com/css2?family=Great+Vibes&family=Parisienne&family=Alex+Brush&family=Delius&display=swap">
<style>
  :root {
    --backdrop: #b1b2b4;
    --paper: #ffffff;
    --rose-ink: #c9909a;
    --rose-line: #d8a7b0;
    --gold: #d9c48e;
    --gold-line: #c9bd93;
    --olive: #8a9a57;
    --berry: #9c3a52;
    --rust: #c8562a;
    --magenta: #b8246a;
    --ink: #2a2a2a;
    --cream: #fbf5e2;
  }
  * { box-sizing: border-box; margin: 0; padding: 0; }
  html, body { width: 1200px; height: 1068px; overflow: hidden; }
  body { background: var(--backdrop); position: relative; }

  .cover {
    position: absolute;
    width: 365px;
    height: 470px;
    background: var(--paper);
    overflow: hidden;
  }
  .cover svg.frame { position: absolute; inset: 0; width: 365px; height: 470px; }
  .cover .art { position: absolute; border-radius: 50%; }
  .cover .title { position: absolute; white-space: nowrap; text-align: center; }

  /* Cover 1 – vintage roses */
  .cover--roses { left: 25px; top: 46px;
    background: radial-gradient(ellipse at 50% 45%, #fbf3f5 0%, #f3ecef 55%, #ffffff 100%); }
  .cover--roses .art--top { left: 54px; top: 59px; width: 182px; height: 129px;
    background: radial-gradient(circle at 45% 45%, #d76c84 0%, #eab3bd 45%, #a9c3a6 80%, transparent 100%); }
  .cover--roses .art--low { left: 168px; top: 318px; width: 91px; height: 47px;
    background: radial-gradient(circle, #d87888 0%, #efc0c6 50%, #b3c9ad 80%, transparent 100%); }
  .cover--roses .title { left: 0; width: 365px; top: 374px; font-family: "Great Vibes", cursive; font-size: 19px; color: var(--ink); }

  /* Cover 2 – golden branch */
  .cover--branch { left: 417px; top: 46px;
    background: linear-gradient(180deg, #ddd2bd 0%, #efe8da 35%, #ffffff 75%); }
  .cover--branch .art--top { left: -20px; top: -20px; width: 270px; height: 160px; border-radius: 0 0 60% 40%;
    background: radial-gradient(ellipse at 50% 40%, #e59a3c 0%, #f0bf6e 40%, rgba(120,140,110,.5) 70%, transparent 100%); }
  .cover--branch .title { left: 0; width: 365px; top: 372px; font-family: "Parisienne", cursive; font-size: 19px; color: var(--rust); }

  /* Cover 3 – wildflower oval */
  .cover--wild { left: 810px; top: 46px;
    background: linear-gradient(110deg, #f3f7ee 0%, #ffffff 30%, #ffffff 60%, #fbefe0 100%); }
  .cover--wild .art--pattern { left: 0; top: 0; width: 365px; height: 470px; border-radius: 0;
    background: linear-gradient(100deg, rgba(205,222,196,.35) 0%, rgba(255,255,255,0) 40%, rgba(245,215,175,.35) 100%); }
  .cover--wild .art--top { left: 41px; top: 53px; width: 147px; height: 112px;
    background: radial-gradient(circle at 50% 50%, #a5253f 0%, #e5c23c 40%, #7f8d52 75%, transparent 100%); }
  .cover--wild .art--low { left: 232px; top: 318px; width: 67px; height: 73px;
    background: radial-gradient(circle, #e8953a 0%, #c2517a 45%, #8a9a57 75%, transparent 100%); }
  .cover--wild .title { left: 0; width: 365px; top: 390px; font-family: "Parisienne", cursive; font-size: 19px; color: var(--berry); }

  /* Cover 4 – line-drawn blossoms */
  .cover--blossom { left: 222px; top: 545px;
    background: linear-gradient(90deg, #ecc3cf 0%, #f6e4ea 30%, #ffffff 55%); }
  .cover--blossom .panel { position: absolute; left: 70px; top: 140px; width: 330px; height: 205px;
    background: linear-gradient(180deg, #fefcfd 0%, #f9eee9 100%); transform: rotate(-6deg); transform-origin: left bottom; }
  .cover--blossom .art--left { left: -30px; top: 122px; width: 130px; height: 229px;
    background: radial-gradient(ellipse at 35% 50%, #d9779f 0%, #eab3c9 45%, rgba(230,190,210,.4) 75%, transparent 100%); }
  .cover--blossom .art--rose { left: 227px; top: 316px; width: 62px; height: 32px;
    background: radial-gradient(circle, #d87888 0%, #eec0c5 50%, #b3c9ad 80%, transparent 100%); }
  .cover--blossom .title { left: 80px; top: 70px; font-family: "Alex Brush", cursive; font-size: 30px; color: var(--magenta); transform: rotate(-9deg); transform-origin: left center; }

  /* Cover 5 – lilac frames */
  .cover--lilac { left: 618px; top: 545px;
    background: radial-gradient(ellipse at 60% 50%, #ffffff 0%, #fdf8ea 55%, #f7eed2 100%); }
  .cover--lilac .art--top { left: 22px; top: 37px; width: 112px; height: 150px;
    background: radial-gradient(ellipse at 55% 60%, #c23d86 0%, #e79bc8 45%, rgba(150,175,120,.45) 75%, transparent 100%); }
  .cover--lilac .art--low { left: 198px; top: 325px; width: 141px; height: 91px;
    background: radial-gradient(ellipse at 65% 55%, #cc4d95 0%, #eab2d2 50%, rgba(150,175,120,.4) 78%, transparent 100%); }
  .cover--lilac .mark { position: absolute; width: 9px; height: 9px; border-radius: 50%; background: var(--magenta); }
  .cover--lilac .title { left: 94px; top: 55px; font-family: "Delius", cursive; font-size: 14.5px; letter-spacing: .3px; color: var(--magenta); }
</style>
</head>
<body>

<section class="cover cover--roses">
  <div class="art art--top" role="img" aria-label="Cluster of pink vintage roses with green leaves"></div>
  <svg class="frame" viewBox="0 0 365 470" aria-hidden="true">
    <ellipse cx="179" cy="238" rx="113" ry="91" fill="none" stroke="var(--rose-line)" stroke-width="2"/>
    <line x1="101" y1="212" x2="252" y2="212" stroke="var(--rose-ink)" stroke-width=".8"/>
    <line x1="101" y1="241" x2="252" y2="241" stroke="var(--rose-ink)" stroke-width=".8"/>
    <path d="M150 330 C 200 300, 270 320, 300 280" fill="none" stroke="var(--rose-line)" stroke-width="1.2"/>
  </svg>
  <div class="art art--low" role="img" aria-label="Small spray of pink roses"></div>
  <p class="title">Speech Therapy Planner</p>
</section>

<section class="cover cover--branch">
  <div class="art art--top" role="img" aria-label="Flowering branch with orange blossoms"></div>
  <svg class="frame" viewBox="0 0 365 470" aria-hidden="true">
    <circle cx="182" cy="250" r="103" fill="none" stroke="var(--gold)" stroke-width="1.5"/>
    <ellipse cx="183" cy="248" rx="108" ry="100" fill="none" stroke="var(--gold)" stroke-width="2.5" stroke-dasharray="480 200"/>
    <line x1="101" y1="235" x2="252" y2="235" stroke="var(--gold-line)" stroke-width=".8"/>
    <line x1="101" y1="265" x2="252" y2="265" stroke="var(--gold-line)" stroke-width=".8"/>
    <path d="M120 322 C 160 290, 210 340, 250 312" fill="none" stroke="var(--gold)" stroke-width="3"/>
  </svg>
  <p class="title">Speech Therapy Planner</p>
</section>

<section class="cover cover--wild">
  <div class="art art--pattern" role="img" aria-label="Soft dashed stripe pattern in green and peach"></div>
  <svg class="frame" viewBox="0 0 365 470" aria-hidden="true">
    <defs>
      <linearGradient id="ovalStroke" x1="0" y1="0" x2="1" y2="1">
        <stop offset="0" stop-color="var(--berry)"/>
        <stop offset="1" stop-color="var(--olive)"/>
      </linearGradient>
    </defs>
    <ellipse cx="181" cy="249" rx="118" ry="142" fill="#ffffff" fill-opacity=".85" stroke="url(#ovalStroke)" stroke-width="1.8"/>
    <line x1="107" y1="216" x2="258" y2="216" stroke="var(--gold-line)" stroke-width=".8"/>
    <line x1="107" y1="245" x2="258" y2="245" stroke="var(--gold-line)" stroke-width=".8"/>
  </svg>
  <div class="art art--top" role="img" aria-label="Bouquet of red and yellow wildflowers"></div>
  <div class="art art--low" role="img" aria-label="Small cluster of orange and purple flowers"></div>
  <p class="title">Speech Therapy Planner</p>
</section>

<section class="cover cover--blossom">
  <div class="panel"></div>
  <div class="art art--left" role="img" aria-label="Line-drawn pink blossoms"></div>
  <svg class="frame" viewBox="0 0 365 470" aria-hidden="true">
    <line x1="135" y1="221" x2="286" y2="221" stroke="var(--rose-ink)" stroke-width=".8"/>
    <line x1="135" y1="250" x2="286" y2="250" stroke="var(--rose-ink)" stroke-width=".8"/>
    <path d="M262 338 C 300 370, 250 400, 270 420 S 240 440, 255 445" fill="none" stroke="#a07f86" stroke-width=".8"/>
  </svg>
  <div class="art art--rose" role="img" aria-label="Small rose spray"></div>
  <p class="title">Speech Therapy Planner</p>
</section>

<section class="cover cover--lilac">
  <svg class="frame" viewBox="0 0 365 470" aria-hidden="true">
    <rect x="64" y="157" width="234" height="196" fill="#ffffff" stroke="#b6a37a" stroke-width="1" transform="rotate(-2 181 255)"/>
    <rect x="62" y="155" width="240" height="198" fill="none" stroke="#c2b18a" stroke-width="1" transform="rotate(1.5 181 255)"/>
    <rect x="66" y="153" width="236" height="200" fill="none" stroke="#cbbd99" stroke-width="1"/>
    <line x1="106" y1="240" x2="257" y2="240" stroke="#a79a84" stroke-width=".8"/>
    <line x1="106" y1="269" x2="257" y2="269" stroke="#a79a84" stroke-width=".8"/>
  </svg>
  <div class="art art--top" role="img" aria-label="Sprig of pink lilac with leaves"></div>
  <div class="art art--low" role="img" aria-label="Sprig of pink lilac"></div>
  <span class="mark" style="left:78px;top:60px"></span>
  <span class="mark" style="left:553px;top:104px;left:319px"></span>
  <span class="mark" style="left:75px;top:375px"></span>
  <p class="title">Speech Therapy Planner</p>
</section>

</body>
</html>
```